Home Security Company Business Card

Looking for a eye catching business card that is non traditional and stands out but yet still looks professional. It should include all the pertinent information such as name, title, address, telephone, e-mail, website address should definitely stand out and then finally the logo.

Target Market(s)

Residential and Commercial accounts mostly upscale accounts

Industry/Entity Type

Security

Contact Information for Business Card

Name
Title
Address
Office #
Cell #
E-mail
Website

Font styles to use
Serif
Sans Serif

Requirements
Must have
• Logo, two sided color configuration
Nice to have
• You decide
Should not have
• There really aren't any.

```html
<!DOCTYPE html>
<html lang="en">
<head>
<meta charset="UTF-8">
<title>Wardcrest Security Systems Inc. – Business Card</title>
<link rel="stylesheet" href="https://fonts.googleapis.com/css2?family=PT+Sans:wght@400;700&family=Tinos&display=swap">
<style>
  :root {
    --stage: #000000;
    --card-front: #f3f3f3;
    --card-back: #7d1518;
    --card-back-glow: #93302a;
    --brand-red: #861a1c;
    --text-dark: #3a3a3a;
    --white: #ffffff;
    --serif: "Tinos", "Times New Roman", serif;
    --sans: "PT Sans", Arial, sans-serif;
  }
  * { margin: 0; padding: 0; box-sizing: border-box; }
  html, body {
    width: 1200px; height: 900px; overflow: hidden;
    background: var(--stage);
  }
  .canvas { position: relative; width: 1200px; height: 900px; }

  .card { position: absolute; top: 200px; width: 310px; height: 502px; }

  .card-front {
    left: 293px;
    background: var(--card-front);
    border-radius: 62px 0 62px 0;
  }
  .card-back {
    left: 613px; width: 309px;
    background: radial-gradient(ellipse 60% 50% at 55% 42%, var(--card-back-glow) 0%, var(--card-back) 75%);
    border-radius: 0 62px 0 62px;
    overflow: hidden;
  }

  /* Front: brand mark */
  .brand {
    position: absolute; left: 56px; top: 86px;
    display: flex; align-items: center; gap: 10px;
  }
  .brand-square { width: 30px; height: 30px; background: var(--brand-red); }
  .brand-name {
    font-family: var(--serif); font-weight: 400; color: var(--brand-red);
    line-height: 1;
  }
  .brand-name .primary { display: block; font-size: 23px; }
  .brand-name .secondary { display: block; font-size: 11px; margin-top: 2px; }

  /* Front: contact block */
  .contact {
    position: absolute; left: 27px; top: 290px;
    font-family: var(--sans); color: var(--text-dark);
    font-size: 14px; line-height: 16px;
  }
  .person-name {
    font-size: 18.5px; font-weight: 700; color: var(--brand-red);
    letter-spacing: 0.2px; line-height: 20px;
  }
  .person-title { margin-top: 4px; }
  .address { margin-top: 18px; }
  .contact-list { list-style: none; margin-top: 11px; }
  .contact-list li { display: flex; align-items: center; gap: 6px; height: 19px; }
  .contact-list svg { width: 10px; height: 10px; fill: var(--brand-red); flex: none; }

  /* Back: company name */
  .back-name {
    position: absolute; left: 33px; top: 373px;
    font-family: var(--serif); font-weight: 400; color: var(--white);
    line-height: 1;
  }
  .back-name .primary { display: block; font-size: 40px; letter-spacing: 0.3px; }
  .back-name .secondary { display: block; font-size: 18.5px; margin-top: 2px; }
</style>
</head>
<body>
<main class="canvas">

  <section class="card card-front" aria-label="Business card front">
    <div class="brand">
      <span class="brand-square" aria-hidden="true"></span>
      <span class="brand-name">
        <span class="primary">WARDCREST</span>
        <span class="secondary">SECURITY SYSTEMS INC.</span>
      </span>
    </div>

    <div class="contact">
      <p class="person-name">DANIEL REYES</p>
      <p class="person-title">Managing Director</p>
      <p class="address">1234, Address Goes Here<br>Country Name, 123456</p>
      <ul class="contact-list">
        <li>
          <svg viewBox="0 0 10 10" aria-hidden="true"><path d="M0 3.5 Q5 0 10 3.5 L8.5 5 L7 4 L7 3 Q5 2.3 3 3 L3 4 L1.5 5 Z M2 5.5 L8 5.5 L9 9 L1 9 Z"/></svg>
          823-456-7890
        </li>
        <li>
          <svg viewBox="0 0 10 10" aria-hidden="true"><path d="M3 0 H7 Q8 0 8 1 V9 Q8 10 7 10 H3 Q2 10 2 9 V1 Q2 0 3 0 Z M3 1.5 V7.5 H7 V1.5 Z"/></svg>
          823-456-7890
        </li>
        <li>
          <svg viewBox="0 0 10 10" aria-hidden="true"><path d="M0 2 H10 V8 H0 Z M0.8 2.6 L5 5.6 L9.2 2.6" fill="var(--brand-red)"/><path d="M0.8 2.6 L5 5.6 L9.2 2.6" fill="none" stroke="#f3f3f3" stroke-width="0.8"/></svg>
          info@youremail.com
        </li>
        <li>
          <svg viewBox="0 0 10 10" aria-hidden="true"><path d="M4 6 L6 4" stroke="var(--brand-red)" stroke-width="1.3" fill="none"/><path d="M5.5 2 L6.5 1 Q7.5 0 8.5 1 L9 1.5 Q10 2.5 9 3.5 L8 4.5 M4.5 8 L3.5 9 Q2.5 10 1.5 9 L1 8.5 Q0 7.5 1 6.5 L2 5.5" stroke="var(--brand-red)" stroke-width="1.3" fill="none"/></svg>
          www.companyname.com
        </li>
      </ul>
    </div>
  </section>

  <section class="card card-back" aria-label="Business card back">
    <div class="back-name">
      <span class="primary">WARDCREST</span>
      <span class="secondary">SECURITY SYSTEMS INC.</span>
    </div>
  </section>

</main>
</body>
</html>
```